Reaching the Root: Reasoning in Clinical Choice-Making

I'd like a cover that looks like it would fit on the shelf next to "The Symptom Mirage" by Harold Vintner, "The Fall of Forgetting" by Carl Mortenson, "Meal Mend" by Neil Forsby, "The Energy Renewal Plan" by Owen Prichardson or "The Gland Renewal Plan" by the same or "The Cortex Renewal Plan" by the same ... either text only (with some interesting fonts that make the title stand out, and the subtitle smaller) or a relevant image, though I'm not entirely sure what that would be since this is a book about big-picture medical decision making.
Author name is Dr Miriam Oakhurst, NMD
I'll eventually request an e-book, paperback, and audio cover from the winner...

Target Market(s)

practicing physicians

Industry/Entity Type

medicine

Requirements
Must have
• look similar to other books in the genre

```html
<!DOCTYPE html>
<html lang="en">
<head>
<meta charset="utf-8">
<title>Reaching the Root: Reasoning in Clinical Choice-Making — Cover</title>
<link rel="stylesheet" href="https://fonts.googleapis.com/css2?family=Bebas+Neue&family=Oswald:wght@500&family=Poppins:wght@400&display=swap">
<style>
  :root {
    --stage: #858585;
    --navy-deep: #031a3d;
    --navy-mid: #0a3b78;
    --glow: #1a78c8;
    --cyan: #00dcea;
    --white: #ffffff;
    --ink: #161616;
    --rule: #9fb3cc;
  }
  html, body {
    margin: 0;
    padding: 0;
    width: 673px;
    height: 1200px;
    overflow: hidden;
    background: var(--stage);
  }
  .stage {
    position: relative;
    width: 673px;
    height: 1200px;
    display: flex;
    align-items: center;
    justify-content: center;
  }
  .book-cover {
    display: block;
    width: 673px;
    height: 1007px;
    box-shadow: 0 8px 24px rgba(0,0,0,0.25);
  }
  .series-line {
    font-family: "Poppins", sans-serif;
    font-weight: 400;
    fill: var(--white);
  }
  .title-condensed {
    font-family: "Bebas Neue", "Oswald", sans-serif;
  }
  .title-white { fill: var(--white); }
  .title-cyan { fill: var(--cyan); }
  .title-rule { stroke: var(--rule); stroke-width: 1; }
  .author-band { fill: var(--white); }
  .author-name {
    font-family: "Oswald", sans-serif;
    font-weight: 500;
    fill: var(--ink);
  }
</style>
</head>
<body>
<main class="stage">
  <svg class="book-cover" viewBox="0 0 685 1025" xmlns="http://www.w3.org/2000/svg" aria-labelledby="cover-title">
    <title id="cover-title">Reaching the Root: Reasoning in Clinical Choice-Making by Dr Miriam Oakhurst, NMD</title>
    <defs>
      <radialGradient id="photo-glow" cx="0.42" cy="0.72" r="0.75">
        <stop offset="0" stop-color="var(--glow)"/>
        <stop offset="0.45" stop-color="var(--navy-mid)"/>
        <stop offset="1" stop-color="var(--navy-deep)"/>
      </radialGradient>
    </defs>

    <rect class="cover-photo" x="0" y="0" width="685" height="912" fill="url(#photo-glow)"
          role="img" aria-label="Close-up photograph of a chrome stethoscope chest piece and dark blue tubing on a deep blue background"/>

    <text class="series-line" x="342.5" y="100" font-size="25" text-anchor="middle"
          textLength="380" lengthAdjust="spacing">REACHING THE ROOT</text>

    <line class="title-rule" x1="88" y1="163" x2="208" y2="163"/>
    <line class="title-rule" x1="477" y1="163" x2="597" y2="163"/>
    <text class="title-condensed title-white" x="342.5" y="200" font-size="100" text-anchor="middle"
          textLength="250" lengthAdjust="spacingAndGlyphs">REASONING IN</text>

    <text class="title-condensed title-cyan" x="343" y="362" font-size="200" text-anchor="middle"
          textLength="536" lengthAdjust="spacingAndGlyphs">CLINICAL</text>

    <text class="title-condensed title-white" x="344" y="452" font-size="100" text-anchor="middle"
          textLength="538" lengthAdjust="spacingAndGlyphs">CHOICE-MAKING</text>

    <rect class="author-band" x="0" y="911" width="685" height="114"/>
    <text class="author-name" x="342.5" y="971" font-size="32" text-anchor="middle"
          textLength="433" lengthAdjust="spacing">DR MIRIAM OAKHURST, NMD</text>
  </svg>
</main>
</body>
</html>
```